design a catchy flyer for my electrical buisness

need a flyer designed to attract people to my business by looking professional and offering specials

Target Market(s)

all people i want to look affordable to everyone but still keeping that professional look and feel

Industry/Entity Type

Electrical

Requirements
Must have
• NO JOB TO BIG OR SMALL
• CALL NOW FOR A FREE QUOTE 0400318726
• NO CALL OUT FEE
• same promises as uploaded pic maybe written different style
• Your neighborhood electrician
• 100% satisfaction guaranteed
• were here to help
• mention this flyer for 10% off
• specializing in house renovations, extensions, kitchen and bathroom upgrades switchboard upgrades
• Make your house safe with our RCD and smoke alarm packages
Nice to have
• modern
• proffesional
• shows trust when customers read it
Should not have
• corny slogans
• cheap look

```html
<!DOCTYPE html>
<html lang="en">
<head>
<meta charset="utf-8">
<title>Your Neighbourhood Electrician – Flyer</title>
<link rel="stylesheet" href="https://fonts.googleapis.com/css2?family=Oswald:wght@400;500;600&family=Questrial&family=Arimo:wght@400;700&display=swap">
<style>
  :root{
    --orange:#f26b1d;
    --orange-deep:#e85a12;
    --red:#f2391f;
    --charcoal:#2e2e2e;
    --light:#f4f4f4;
    --light-edge:#dcdcdc;
    --white:#ffffff;
    --ink:#222222;
    --page:#e4e4e4;
    --photo-top:#8a8fa8;
    --photo-bottom:#4a5590;
  }
  *{margin:0;padding:0;box-sizing:border-box}
  html,body{width:825px;height:1200px;overflow:hidden;background:var(--page)}
  .flyer{
    position:absolute;left:0;top:15px;width:662px;height:938px;
    transform:scale(1.2462);transform-origin:0 0;
    overflow:hidden;background:var(--light);
    font-family:"Arimo",Arial,sans-serif;
  }
  .shapes{position:absolute;inset:0}
  .photo{
    position:absolute;left:12px;top:12px;width:305px;height:400px;
    background:linear-gradient(180deg,var(--photo-top) 0%,var(--photo-bottom) 100%);
    opacity:.9;
  }
  .title{position:absolute;right:35px;top:28px;text-align:right;font-family:"Questrial",sans-serif;color:var(--ink);white-space:nowrap}
  .title .small{font-size:33px;line-height:1}
  .title .big{font-size:57px;line-height:1.05;color:var(--orange)}
  .satisfaction{position:absolute;left:375px;top:185px;width:260px}
  .satisfaction svg{position:absolute;left:-10px;top:0}
  .satisfaction .text{position:absolute;left:88px;top:2px;font-family:"Oswald",sans-serif;text-transform:uppercase;white-space:nowrap}
  .satisfaction .line1{color:var(--white);font-size:21px;line-height:1.1;letter-spacing:.3px}
  .satisfaction .line2{color:var(--orange);font-size:35px;line-height:1.05;font-weight:500}
  .brand{position:absolute;left:418px;top:318px;display:flex;align-items:center;gap:10px}
  .brand .dot{width:30px;height:30px;border-radius:50%;background:var(--orange)}
  .brand .name{font-family:"Questrial",sans-serif;font-size:22px;color:#666}
  .promises{position:absolute;left:32px;top:452px;list-style:none}
  .promises li{font-family:"Questrial",sans-serif;font-size:17px;color:var(--ink);line-height:30px;padding-left:18px;position:relative;text-transform:uppercase;white-space:nowrap}
  .promises li::before{content:"";position:absolute;left:0;top:10px;width:9px;height:9px;border-radius:50%;background:var(--orange)}
  .badge{position:absolute;border-radius:50%;background:var(--red);border:9px solid var(--white);box-shadow:0 0 0 2px var(--light-edge),0 3px 6px rgba(0,0,0,.25);display:flex;flex-direction:column;align-items:center;justify-content:center;text-align:center;color:var(--white);font-family:"Oswald",sans-serif;text-transform:uppercase;line-height:1.1;white-space:nowrap}
  .badge.fixed{left:428px;top:390px;width:186px;height:186px;font-size:27px;font-weight:500}
  .badge.ontime{left:228px;top:507px;width:134px;height:134px;font-size:17px;font-weight:500}
  .badge.quality{left:45px;top:555px;width:142px;height:142px;font-size:27px;font-weight:500}
  .badge.quality .sub{font-size:16px}
  .discount{position:absolute;left:385px;top:615px;width:277px;height:75px;background:var(--orange);clip-path:polygon(8% 0,100% 0,100% 100%,0 100%);display:flex;align-items:center;justify-content:center;color:var(--white);font-family:"Oswald",sans-serif;font-weight:500;font-size:44px;padding-left:10px}
  .packages{position:absolute;left:30px;top:718px;width:610px}
  .packages h2{font-family:"Oswald",sans-serif;font-weight:500;font-size:19.5px;color:var(--orange);text-transform:uppercase;line-height:1.15;white-space:nowrap}
  .packages .services{font-size:12.2px;color:var(--white);margin-top:3px;white-space:nowrap}
  .commitments{position:absolute;top:783px;list-style:none}
  .commitments.left{left:30px}
  .commitments.right{left:330px}
  .commitments li{font-size:11.2px;color:#e6e6e6;line-height:16.4px;padding-left:17px;position:relative;white-space:nowrap}
  .commitments li::before{content:"";position:absolute;left:0;top:4px;width:8px;height:8px;border-radius:50%;background:var(--orange)}
  .footer{position:absolute;left:0;right:0;top:887px;height:51px;background:var(--orange);border-top:3px solid var(--white);display:flex;align-items:center;justify-content:center;color:var(--white);font-family:"Questrial",sans-serif;font-size:17px;white-space:nowrap}
</style>
</head>
<body>
<main class="flyer">
  <svg class="shapes" viewBox="0 0 662 938" width="662" height="938" aria-hidden="true">
    <defs>
      <linearGradient id="lightFade" x1="0" y1="0" x2="1" y2="0">
        <stop offset="0" stop-color="#ffffff"/><stop offset="1" stop-color="#e2e2e2"/>
      </linearGradient>
      <linearGradient id="orangeFade" x1="0" y1="0" x2="1" y2="1">
        <stop offset="0" stop-color="#f47a22"/><stop offset="1" stop-color="#e8560f"/>
      </linearGradient>
    </defs>
    <rect width="662" height="938" fill="url(#lightFade)"/>
    <polygon points="0,0 200,0 425,415 0,415" fill="url(#orangeFade)"/>
    <polygon points="205,70 222,70 440,415 423,415" fill="#2e2e2e"/>
    <polygon points="293,154 662,154 662,160 297,160" fill="#f26b1d"/>
    <polygon points="297,160 662,160 662,280 362,280" fill="#2e2e2e"/>
    <polygon points="362,280 662,280 662,285 365,285" fill="#f26b1d"/>
    <rect x="0" y="415" width="662" height="5" fill="#f26b1d"/>
    <polygon points="0,645 662,395 662,425 0,675" fill="#f26b1d"/>
    <polygon points="0,675 662,425 662,938 0,938" fill="#2e2e2e"/>
  </svg>

  <div class="photo" role="img" aria-label="Portrait photo of the electrician, arms crossed"></div>

  <header class="title">
    <div class="small">Your Neighbourhood</div>
    <div class="big">Electrician</div>
  </header>

  <div class="satisfaction">
    <svg width="78" height="62" viewBox="0 0 78 62" aria-hidden="true">
      <path d="M6 26h14v32H6z M20 28 L34 8 Q38 2 42 6 Q44 10 41 18 L38 24 H64 Q70 24 70 30 Q70 34 66 35 Q71 37 69 42 Q67 45 64 45 Q68 48 65 52 Q63 54 60 54 Q62 58 58 59 H28 L20 56" fill="none" stroke="#fff" stroke-width="4" stroke-linejoin="round"/>
    </svg>
    <div class="text">
      <div class="line1">100% Satisfaction</div>
      <div class="line2">Guaranteed</div>
    </div>
  </div>

  <div class="brand">
    <span class="dot"></span>
    <span class="name">VoltLine</span>
  </div>

  <ul class="promises">
    <li>No job to big or small</li>
    <li>Were here to help</li>
    <li>No call out fee</li>
  </ul>

  <div class="badge fixed"><span>Fixed Price</span><span>Guarantee</span></div>
  <div class="badge ontime"><span>100% On Time</span><span>Guarantee</span></div>
  <div class="badge quality"><span>Quality</span><span class="sub">Guarantee</span></div>

  <div class="discount">10% OFF</div>

  <section class="packages">
    <h2>Make your house safe with our RCD and smoke alarm packages</h2>
    <p class="services">Specializing in house renovations, extensions, kitchen and bathroom upgrades switchboard upgrades</p>
  </section>

  <ul class="commitments left">
    <li>We will arrive on time or we will pay you $100</li>
    <li>Before any job begins you will know the exact cost</li>
    <li>We will provide you with a fixed price</li>
    <li>guarantee assuring no extra costs</li>
    <li>We will leave your place as clean as when we arrived</li>
  </ul>
  <ul class="commitments right">
    <li>If there is a problem and it's our fault we will fix it for free</li>
    <li>We will return your telephone calls promptly</li>
    <li>We will provide a 12 Month warranty on all parts</li>
    <li>We will provide friendly, helpful service and advice</li>
  </ul>

  <footer class="footer">CALL NOW FOR A FREE QUOTE 0400318726 &nbsp;|&nbsp; callasparky.com.au</footer>
</main>
</body>
</html>
```